The design should be a multi-page, foldable flyer with the logo and the product name on the front and the web address on the back.
DoLMUO is a word play on "zebra", which the design should reflect in some way.

Target Market(s)

Schools and individual teachers

Industry/Entity Type

Product

Colors
ffffff
000000

```html
<!DOCTYPE html>
<html lang="en">
<head>
<meta charset="utf-8">
<title>DoLMUO Folded Flyer</title>
<link href="https://fonts.googleapis.com/css2?family=Arimo:wght@400&family=Hind:wght@600&display=swap" rel="stylesheet">
<style>
  :root {
    --ink: #000000;
    --paper: #ffffff;
    --panel-dark: #2d2d2d;
    --mark-grey: #555555;
    --soft-grey: #a9a9a9;
    --rule-grey: #d4d4d4;
    --stripe-grey: #d9d9d9;
    --headline: #2a2a2a;
  }
  html, body {
    margin: 0;
    padding: 0;
    overflow: hidden;
    background: var(--paper);
  }
  .flyer {
    position: relative;
    width: 1200px;
    height: 849px;
    overflow: hidden;
    background: var(--paper);
    font-family: "Arimo", Arial, sans-serif;
  }
  .back-panel {
    position: absolute;
    left: 0; top: 0;
    width: 600px; height: 560px;
    background: var(--panel-dark);
  }
  .back-panel--lower {
    top: 699px;
    height: 150px;
  }
  .back-panel__mark {
    position: absolute;
    left: 0; width: 600px;
    top: 320px;
    text-align: center;
    font-size: 38px;
    line-height: 1;
    color: var(--mark-grey);
    letter-spacing: 2px;
  }
  .stripe-column {
    position: absolute;
    left: 656px;
    width: 163px;
    background: linear-gradient(180deg, var(--stripe-grey), #e6e6e6);
  }
  .stripe-column--top { top: 0; height: 557px; }
  .stripe-column--bottom { top: 703px; height: 146px; }
  .band {
    position: absolute;
    left: 0; top: 560px;
    width: 1200px; height: 139px;
    background: var(--paper);
  }
  .band__rule {
    position: absolute;
    left: 600px; width: 600px; height: 1px;
    background: var(--rule-grey);
  }
  .band__rule--top { top: 0; }
  .band__rule--bottom { bottom: 0; }
  .back-info {
    position: absolute;
    left: 0; width: 600px; top: 0;
    text-align: center;
  }
  .back-info__name {
    margin: 20px 0 0;
    font-size: 33px;
    font-weight: 400;
    color: var(--soft-grey);
    line-height: 1;
  }
  .back-info__tagline {
    margin: 9px 0 0;
    font-size: 14px;
    line-height: 16px;
    color: var(--soft-grey);
  }
  .back-info__divider {
    display: block;
    margin: 8px auto 0;
  }
  .back-info__web {
    margin: 12px 0 0;
    font-size: 16px;
    line-height: 18px;
    color: var(--ink);
  }
  .front-mark {
    position: absolute;
    left: 706px; top: 42px;
    display: flex;
    align-items: center;
  }
  .front-mark__dot {
    width: 54px; height: 54px;
    border-radius: 50%;
    background: var(--mark-grey);
    margin-right: 18px;
  }
  .front-mark__name {
    font-size: 42px;
    line-height: 1;
    color: var(--mark-grey);
    letter-spacing: 1px;
  }
  .front-mark__tagline {
    font-size: 8px;
    color: var(--mark-grey);
    margin-top: 4px;
    margin-left: 2px;
  }
  .headline {
    position: absolute;
    left: 847px; top: 322px;
    margin: 0;
    list-style: none;
    padding: 0;
    font-family: "Hind", Arial, sans-serif;
    font-weight: 600;
    font-size: 38px;
    line-height: 44.5px;
    color: var(--headline);
  }
</style>
</head>
<body>
<main class="flyer">
  <section class="back-panel">
    <div class="back-panel__mark">DoLMUO</div>
  </section>
  <div class="back-panel back-panel--lower"></div>

  <div class="stripe-column stripe-column--top" role="img" aria-label="Vertical band of light grey zebra stripe pattern"></div>
  <div class="stripe-column stripe-column--bottom" role="img" aria-label="Vertical band of light grey zebra stripe pattern"></div>

  <ul class="headline">
    <li>Plan</li>
    <li>Teach</li>
    <li>Review</li>
    <li>Assess</li>
    <li>Organise</li>
  </ul>

  <section class="band">
    <div class="band__rule band__rule--top"></div>
    <div class="band__rule band__rule--bottom"></div>

    <div class="back-info">
      <p class="back-info__name">DoLMUO</p>
      <p class="back-info__tagline">Plan Teach Review Assess &amp; Organise</p>
      <svg class="back-info__divider" width="290" height="10" viewBox="0 0 290 10" aria-hidden="true">
        <line x1="0" y1="5" x2="127" y2="5" stroke="#d4d4d4" stroke-width="1.5"/>
        <circle cx="145" cy="5" r="3.5" fill="#b5b5b5"/>
        <line x1="162" y1="5" x2="290" y2="5" stroke="#d4d4d4" stroke-width="1.5"/>
      </svg>
      <p class="back-info__web">www.dolmuo.example</p>
    </div>

    <div class="front-mark">
      <div class="front-mark__dot"></div>
      <div>
        <div class="front-mark__name">DoLMUO</div>
        <div class="front-mark__tagline">Plan Teach Review Assess &amp; Organise</div>
      </div>
    </div>
  </section>
</main>
</body>
</html>
```